Flyer für Immobilienmakler
Top Arbeit vom Designer. Er hat alle Idee schnell und professionell umgesetzt und das Ergebnis kann sich sehen lassen. Herzlichen Dank für die großartige Arbeit. Immer wieder gerne.
Zielgruppe
Immobilienmakler, Zielgruppe sind Menschen die uns weiterempfehlen um ihre Immobilie zu verkaufen
Aufgabenstellung
Ein Flyer DIN lang quer, Vorder und Rückseite, Es geht um eine Tippgeberprovision welche Menschen bekommen die uns einen Verkaufskunden bringen, diese erhalten 10 %- genaue Texte und Hinweise werde ich einbringen, Unser Slogan: 'Unsere Erfahrung für Ihren Vorteil'
Nachtrag. Bei dem Flyer 'Vom Berg Immobilien' finde ich die blauen Banner/ Streifen gut- ist aber kein Muss. Update: Es war als Inspiration von meiner Seite gedacht. Auf keinen Fall darf es genauso aussehen!!
Meine jetzige Webseite ist auch gut um die Farben zu erkennen, jedoch nicht unbedingt das Design, da ich gerade eine neue Webseite erstellen lasse

```html
<!DOCTYPE html>
<html lang="de">
<head>
<meta charset="utf-8">
<title>Lumara Immobilien – Tippgeber-Flyer</title>
<link href="https://fonts.googleapis.com/css2?family=Poppins:wght@400;600;700&display=swap" rel="stylesheet">
<style>
  :root {
    --navy: #2a2f63;
    --navy-deep: #132b5e;
    --beige: #c2b19f;
    --paper: #f5f4f2;
    --paper-top: #e4e4e4;
    --ink: #4a4a4a;
    --white: #ffffff;
    --stage: #999999;
  }
  * { margin: 0; padding: 0; box-sizing: border-box; }
  html, body { width: 1200px; height: 1117px; overflow: hidden; }
  body { background: var(--stage); font-family: "Poppins", sans-serif; position: relative; }

  .flyer {
    position: absolute; left: 104px; width: 992px; height: 496px;
    background: linear-gradient(180deg, var(--paper-top) 0%, var(--paper) 35%, var(--paper) 100%);
    box-shadow: 0 6px 14px rgba(0,0,0,0.28);
    overflow: hidden;
  }
  .flyer--front { top: 48px; }
  .flyer--back { top: 573px; height: 495px; background: var(--paper); }
  .flyer__shapes { position: absolute; inset: 0; }

  .brand { position: absolute; left: 67px; top: 52px; color: var(--navy); font-weight: 600; }
  .brand__name { display: block; font-size: 84px; line-height: 1; letter-spacing: 4px; }
  .brand__sub { display: block; font-size: 25px; line-height: 1; margin-top: 10px; margin-left: 242px; }

  .slogan {
    position: absolute; left: 602px; top: 32px; width: 370px;
    color: var(--white); font-weight: 700; font-size: 20px; letter-spacing: 0.2px;
  }
  .slogan__dot { color: var(--beige); margin: 0 8px; }

  .headline {
    position: absolute; left: 66px; top: 198px;
    color: var(--navy); font-weight: 700; font-size: 38px; line-height: 51px;
  }
  .lead {
    position: absolute; left: 67px; top: 307px; width: 340px;
    color: var(--ink); font-size: 19.5px; line-height: 26px;
  }

  .contact-bar {
    position: absolute; left: 0; right: 0; bottom: 0; height: 75px;
    display: flex; align-items: center; color: var(--white); font-size: 24px;
  }
  .contact-bar__item { position: absolute; top: 0; height: 75px; display: flex; align-items: center; }
  .contact-bar__item svg { width: 25px; height: 25px; margin-right: 18px; }
  .contact-bar__item--phone { left: 65px; }
  .contact-bar__item--mail { left: 394px; }
  .contact-bar__item--web { left: 744px; font-weight: 700; }
  .contact-bar__divider { position: absolute; top: 17px; width: 2px; height: 35px; background: var(--white); }

  .offer__intro {
    position: absolute; left: 558px; top: 42px;
    color: var(--beige); font-weight: 700; font-size: 68px; line-height: 1;
  }
  .offer__rate {
    position: absolute; left: 552px; top: 104px;
    color: var(--navy); font-weight: 700; font-size: 148px; line-height: 1; letter-spacing: -6px;
  }
  .offer__text {
    position: absolute; left: 562px; top: 252px; width: 400px;
    color: var(--ink); font-size: 18.5px; line-height: 21.5px;
  }
  .offer__text strong { color: var(--navy-deep); font-weight: 700; }

  .benefits { position: absolute; left: 562px; top: 335px; display: flex; gap: 22px; list-style: none; }
  .benefits__item {
    position: relative; width: 176px; padding-left: 24px;
    color: var(--ink); font-size: 11px; line-height: 15.5px;
  }
  .benefits__item svg { position: absolute; left: 0; top: 2px; width: 13px; height: 13px; }
</style>
</head>
<body>

<section class="flyer flyer--front">
  <svg class="flyer__shapes" viewBox="0 0 992 496" width="992" height="496">
    <defs>
      <linearGradient id="housesTone" x1="0" y1="0" x2="0" y2="1">
        <stop offset="0" stop-color="#c9d2e4"/>
        <stop offset="0.35" stop-color="#e8e4e0"/>
        <stop offset="0.62" stop-color="#d8cfc6"/>
        <stop offset="0.8" stop-color="#7d8a5a"/>
        <stop offset="1" stop-color="#a9a7a3"/>
      </linearGradient>
    </defs>
    <rect x="0" y="0" width="992" height="14" fill="var(--navy)"/>
    <path d="M548 14 C500 120 455 260 462 413 L992 413 L992 14 Z" fill="var(--beige)"/>
    <path d="M580 40 C520 140 475 270 478 413 L992 413 L992 40 Z" fill="var(--white)"/>
    <path d="M586 52 C528 150 484 275 486 413 L992 413 L992 52 Z" fill="url(#housesTone)" role="img" aria-label="Foto: moderne weiße Reihenhäuser mit Carports und Gräsern"/>
    <path d="M510 14 C545 14 560 30 578 52 C598 76 612 84 640 84 L992 84 L992 14 Z" fill="var(--white)"/>
    <path d="M516 14 C548 14 563 28 580 48 C600 72 614 78 640 78 L992 78 L992 0 L516 0 Z" fill="var(--navy)"/>
    <rect x="0" y="413" width="992" height="8" fill="var(--beige)"/>
    <rect x="0" y="421" width="992" height="75" fill="var(--navy-deep)"/>
  </svg>

  <div class="brand">
    <span class="brand__name">LUMARA</span>
    <span class="brand__sub">Immobilien</span>
  </div>

  <p class="slogan">Regional<span class="slogan__dot">•</span>Diskret<span class="slogan__dot">•</span>Individuell.</p>

  <h1 class="headline">Unsere Erfahrung<br>für Ihren Vorteil</h1>
  <p class="lead">Wir unterstützen Sie im gesamten Prozess mit unserem einzigartigen Modulsystem.</p>

  <footer class="contact-bar">
    <span class="contact-bar__item contact-bar__item--phone">
      <svg viewBox="0 0 24 24"><circle cx="12" cy="12" r="12" fill="var(--beige)"/><path d="M8.2 5.5l2 2.6c.3.4.2.9-.1 1.2l-1 1c.8 1.7 2.1 3 3.8 3.8l1-1c.3-.3.8-.4 1.2-.1l2.6 2c.4.3.4.9.1 1.3l-1.2 1.2c-.6.6-1.5.8-2.3.5-3.7-1.3-6.6-4.2-7.9-7.9-.3-.8-.1-1.7.5-2.3l1.2-1.2c.4-.3 1-.3 1.3.1z" fill="var(--navy-deep)"/></svg>
      +49 (0)6123 4567890
    </span>
    <span class="contact-bar__divider" style="left:371px"></span>
    <span class="contact-bar__item contact-bar__item--mail">
      <svg viewBox="0 0 24 24"><circle cx="12" cy="12" r="12" fill="var(--beige)"/><rect x="6" y="8" width="12" height="8.5" rx="0.8" fill="none" stroke="var(--navy-deep)" stroke-width="1.3"/><path d="M6.3 8.4l5.7 4.6 5.7-4.6" fill="none" stroke="var(--navy-deep)" stroke-width="1.3"/></svg>
      kontakt@lumara.immo
    </span>
    <span class="contact-bar__divider" style="left:723px"></span>
    <span class="contact-bar__item contact-bar__item--web">
      <svg viewBox="0 0 24 24"><circle cx="12" cy="12" r="12" fill="var(--beige)"/><g fill="none" stroke="var(--navy-deep)" stroke-width="1.2"><circle cx="12" cy="12" r="6.5"/><ellipse cx="12" cy="12" rx="3" ry="6.5"/><path d="M5.5 12h13M6.5 9h11M6.5 15h11"/></g></svg>
      lumara.immo
    </span>
  </footer>
</section>

<section class="flyer flyer--back">
  <svg class="flyer__shapes" viewBox="0 0 992 495" width="992" height="495">
    <defs>
      <linearGradient id="kitchenTone" x1="0" y1="0" x2="1" y2="1">
        <stop offset="0" stop-color="#e9e7e3"/>
        <stop offset="0.45" stop-color="#d9d2c8"/>
        <stop offset="0.7" stop-color="#a86a3a"/>
        <stop offset="1" stop-color="#c9bba8"/>
      </linearGradient>
    </defs>
    <rect x="0" y="0" width="992" height="14" fill="var(--navy)"/>
    <rect x="0" y="14" width="992" height="8" fill="var(--beige)"/>
    <path d="M0 22 L466 22 C520 120 545 290 530 414 L0 414 Z" fill="var(--beige)"/>
    <path d="M0 22 L434 22 C500 120 528 290 514 414 L0 414 Z" fill="var(--white)"/>
    <path d="M0 22 L424 22 C490 120 518 290 504 414 L0 414 Z" fill="url(#kitchenTone)" role="img" aria-label="Foto: helle moderne Küche mit Holzfronten und Kühlschrank"/>
    <rect x="0" y="414" width="992" height="7" fill="var(--beige)"/>
    <rect x="0" y="421" width="992" height="74" fill="var(--navy-deep)"/>
  </svg>

  <p class="offer__intro">Erhalten</p>
  <p class="offer__rate">10%-</p>
  <p class="offer__text">indem Sie es den Menschen empfehlen, die Ihnen am nächsten stehen <strong>ihr Eigentum an uns zu verkaufen</strong></p>

  <ul class="benefits">
    <li class="benefits__item">
      <svg viewBox="0 0 14 14"><circle cx="7" cy="7" r="7" fill="var(--beige)"/><path d="M4 7.2l2 2 4-4.2" fill="none" stroke="var(--white)" stroke-width="1.6"/></svg>
      Lorem ipsum dolor sit amet, consectetur adipiscing elit sed do eiusmod tempor incididunt ut labore
    </li>
    <li class="benefits__item">
      <svg viewBox="0 0 14 14"><circle cx="7" cy="7" r="7" fill="var(--beige)"/><path d="M4 7.2l2 2 4-4.2" fill="none" stroke="var(--white)" stroke-width="1.6"/></svg>
      Lorem ipsum dolor sit amet, consectetur adipiscing elit sed do eiusmod tempor incididunt ut labore
    </li>
  </ul>

  <footer class="contact-bar">
    <span class="contact-bar__item contact-bar__item--phone">
      <svg viewBox="0 0 24 24"><circle cx="12" cy="12" r="12" fill="var(--beige)"/><path d="M8.2 5.5l2 2.6c.3.4.2.9-.1 1.2l-1 1c.8 1.7 2.1 3 3.8 3.8l1-1c.3-.3.8-.4 1.2-.1l2.6 2c.4.3.4.9.1 1.3l-1.2 1.2c-.6.6-1.5.8-2.3.5-3.7-1.3-6.6-4.2-7.9-7.9-.3-.8-.1-1.7.5-2.3l1.2-1.2c.4-.3 1-.3 1.3.1z" fill="var(--navy-deep)"/></svg>
      +49 (0)6123 4567890
    </span>
    <span class="contact-bar__divider" style="left:371px"></span>
    <span class="contact-bar__item contact-bar__item--mail">
      <svg viewBox="0 0 24 24"><circle cx="12" cy="12" r="12" fill="var(--beige)"/><rect x="6" y="8" width="12" height="8.5" rx="0.8" fill="none" stroke="var(--navy-deep)" stroke-width="1.3"/><path d="M6.3 8.4l5.7 4.6 5.7-4.6" fill="none" stroke="var(--navy-deep)" stroke-width="1.3"/></svg>
      kontakt@lumara.immo
    </span>
    <span class="contact-bar__divider" style="left:723px"></span>
    <span class="contact-bar__item contact-bar__item--web">
      <svg viewBox="0 0 24 24"><circle cx="12" cy="12" r="12" fill="var(--beige)"/><g fill="none" stroke="var(--navy-deep)" stroke-width="1.2"><circle cx="12" cy="12" r="6.5"/><ellipse cx="12" cy="12" rx="3" ry="6.5"/><path d="M5.5 12h13M6.5 9h11M6.5 15h11"/></g></svg>
      lumara.immo
    </span>
  </footer>
</section>

</body>
</html>
```